Cellarqueen Pamphlet

We need to design a pamplet for Cellarqueen, a Bespoke Wine Cellar design and build company. Our logo and signature cellar should be incorperated into the design (can be seen at www.cellarqueen-example.com). It should also include what will be called the template with a scematic drawing of a cellar to outline the key features An area called the process will showcase the different types of materials that can be used and there neesa to be indicative costs dependant in size also somewhere, as well as the fact that design £950+VAT but will be taken off the cost of the cellar if we do the job refunded back into project on approval.
.

```html
<!DOCTYPE html>
<html lang="en">
<head>
<meta charset="utf-8">
<title>Cellarqueen – Bespoke Wine Cellars Pamphlet</title>
<link rel="stylesheet" href="https://fonts.googleapis.com/css2?family=Didact+Gothic&family=Questrial&display=swap">
<style>
  :root {
    --bg: #050505;
    --bg-soft: #121212;
    --text-strong: #e6e6e6;
    --text-body: #7a7a7a;
    --text-muted: #5a5a5a;
    --text-foot: #4e4e4e;
    --rule: rgba(255,255,255,0.05);
    --badge-bg: #1a1a1a;
  }
  * { margin: 0; padding: 0; box-sizing: border-box; }
  html, body { width: 1200px; height: 849px; overflow: hidden; background: var(--bg); }
  .pamphlet {
    position: relative; width: 1200px; height: 849px; overflow: hidden;
    background: linear-gradient(160deg, #0d0d0d 0%, var(--bg) 45%, #080808 100%);
    font-family: "Didact Gothic", "Questrial", sans-serif;
    color: var(--text-body);
  }
  .fold-rule {
    position: absolute; top: 0; bottom: 0; width: 0;
    border-left: 2px dotted var(--rule);
  }
  .fold-rule.one { left: 398px; }
  .fold-rule.two { left: 762px; }

  .brand-name {
    position: absolute; left: 58px; top: 54px;
    font-family: "Questrial", sans-serif; font-size: 19px; letter-spacing: 5px;
    color: var(--text-strong);
  }
  .tagline { position: absolute; left: 58px; top: 113px; }
  .tagline .service { font-size: 12px; color: var(--text-muted); }
  .tagline .city { font-size: 20px; color: var(--text-muted); margin-top: 4px; }

  .intro {
    position: absolute; left: 58px; top: 224px; width: 282px;
    font-size: 11px; line-height: 21.2px; letter-spacing: 2.1px;
    color: var(--text-body); text-align: justify;
  }
  .intro p { margin-bottom: 15px; }
  .intro .design-fee { margin-top: 6px; font-size: 10.5px; color: var(--text-muted); }

  .hero-drawing {
    position: absolute; left: 460px; top: 57px; width: 740px; height: 228px;
    background: linear-gradient(120deg, #8f8c87 0%, #d8d6d1 30%, #efeeea 55%, #c9c6c0 80%, #9a9791 100%);
  }

  .process { position: absolute; left: 460px; top: 332px; width: 480px; }
  .process h2 { font-weight: normal; font-size: 17px; color: var(--text-strong); }
  .process p { margin-top: 12px; font-size: 11.5px; line-height: 21px; letter-spacing: 0.4px; color: var(--text-muted); }

  .brand-badge {
    position: absolute; left: 1015px; top: 350px; width: 185px; height: 50px;
    background: var(--badge-bg);
    display: flex; align-items: center; gap: 10px; padding-left: 20px;
    font-family: "Questrial", sans-serif; font-size: 13px; letter-spacing: 2.5px;
    color: var(--text-strong);
  }
  .brand-badge .mark { width: 10px; height: 10px; background: var(--text-strong); }

  .materials { position: absolute; top: 455px; }
  .materials.woods { left: 460px; }
  .materials.stones { left: 740px; }
  .materials.glass { left: 1015px; }
  .material { position: relative; height: 57px; width: 185px; }
  .material .name { font-size: 13px; color: var(--text-strong); line-height: 16px; }
  .material .spec { font-size: 9.5px; color: var(--text-foot); margin-top: 6px; letter-spacing: 0.3px; }
  .material .swatch { position: absolute; left: 134px; top: 2px; width: 50px; height: 50px; }

  .footer {
    position: absolute; left: 0; right: 0; top: 828px; text-align: center;
    font-size: 11.5px; color: var(--text-foot); letter-spacing: 0.4px;
    padding-left: 0; transform: translateX(1px);
  }
  .footer span { margin: 0 4px; }
</style>
</head>
<body>
<main class="pamphlet">
  <div class="fold-rule one"></div>
  <div class="fold-rule two"></div>

  <div class="brand-name">CELLARQUEEN</div>
  <div class="tagline">
    <div class="service">Bespoke Wine Cellars</div>
    <div class="city">London</div>
  </div>

  <section class="intro">
    <p>CELLARQUEEN combines custom artistic home wine cellar design with elegance and engineering to produce wine storage known for its extravagance, architecture and identity.</p>
    <p>Every bespoke wine cellar design is unique and individual according to your taste.</p>
    <p>Rich hard wood, hand stitched leather, a spiral wine cellar, beautiful lighting displays and seamless glass finish to display your magnificent collection of wines, champagnes and cigars...</p>
    <p>Bespoke Climate Controlled Wine Rooms and Home Wine Cellar Systems Installation With Humidity Control.</p>
    <p>The possibility of an climate controlled wine cellar for your wine storage may be the perfect way to increase the value of your home, in the way only a wine cellar can add.</p>
    <p>.....</p>
    <p class="design-fee">Design costs of £950+VAT will be refunded back into the project opon approval.</p>
  </section>

  <div class="hero-drawing" role="img" aria-label="Photograph of rolled architectural cellar plans at 1:50 scale"></div>

  <section class="process">
    <h2>The Process</h2>
    <p>Choose from our exclusive materials list, and have our luxury design team and specialist consultants come out and design your bespoke wine cellar today.</p>
  </section>

  <div class="brand-badge"><span class="mark"></span>CELLARQUEEN</div>

  <div class="materials woods">
    <div class="material"><div class="name">Masur</div><div class="spec">Birch &nbsp;. &nbsp;00.00$ m2</div><div class="swatch" role="img" aria-label="Masur birch wood sample" style="background:linear-gradient(135deg,#c79a5e,#8f6431)"></div></div>
    <div class="material"><div class="name">Carpathian</div><div class="spec">Elm &nbsp;. &nbsp;00.00$ m2</div><div class="swatch" role="img" aria-label="Carpathian elm wood sample" style="background:linear-gradient(135deg,#8c5526,#5a3115)"></div></div>
    <div class="material"><div class="name">Zebrawood</div><div class="spec">Exotic &nbsp;. &nbsp;00.00$ m2</div><div class="swatch" role="img" aria-label="Zebrawood sample" style="background:linear-gradient(90deg,#c9a27a,#8a6444,#d1ad86)"></div></div>
    <div class="material"><div class="name">Burmese</div><div class="spec">Exotic &nbsp;. &nbsp;00.00$ m2</div><div class="swatch" role="img" aria-label="Burmese wood sample" style="background:linear-gradient(135deg,#6b5638,#3f3322)"></div></div>
    <div class="material"><div class="name">Bocote</div><div class="spec">Exotic &nbsp;. &nbsp;00.00$ m2</div><div class="swatch" role="img" aria-label="Bocote wood sample" style="background:linear-gradient(135deg,#8a6236,#3e2812)"></div></div>
    <div class="material"><div class="name">Brownheart</div><div class="spec">Exotic &nbsp;. &nbsp;00.00$ m2</div><div class="swatch" role="img" aria-label="Brownheart wood sample" style="background:linear-gradient(135deg,#7d6a4e,#55452f)"></div></div>
  </div>

  <div class="materials stones">
    <div class="material"><div class="name">Granada</div><div class="spec">Granite &nbsp;. &nbsp;00.00$ m2</div><div class="swatch" role="img" aria-label="Granada granite sample" style="background:linear-gradient(135deg,#b9b6b0,#8a8782)"></div></div>
    <div class="material"><div class="name">Breccia Dark</div><div class="spec">Limestone &nbsp;. &nbsp;00.00$ m2</div><div class="swatch" role="img" aria-label="Breccia Dark limestone sample" style="background:linear-gradient(135deg,#d6b27a,#a9814c)"></div></div>
    <div class="material"><div class="name">Breccia</div><div class="spec">Limestone &nbsp;. &nbsp;00.00$ m2</div><div class="swatch" role="img" aria-label="Breccia limestone sample" style="background:linear-gradient(135deg,#c59c62,#8d6a3c)"></div></div>
    <div class="material"><div class="name">Crema Marfil</div><div class="spec">Marble &nbsp;. &nbsp;00.00$ m2</div><div class="swatch" role="img" aria-label="Crema Marfil marble sample" style="background:linear-gradient(135deg,#a99a80,#77695a)"></div></div>
    <div class="material"><div class="name">Emperador Dark</div><div class="spec">Marble &nbsp;. &nbsp;00.00$ m2</div><div class="swatch" role="img" aria-label="Emperador Dark marble sample" style="background:linear-gradient(135deg,#5a3a22,#2a1a10)"></div></div>
    <div class="material"><div class="name">Nero Maquena</div><div class="spec">Marble &nbsp;. &nbsp;00.00$ m2</div><div class="swatch" role="img" aria-label="Nero Maquena marble sample" style="background:linear-gradient(135deg,#d0a868,#a57f45)"></div></div>
  </div>

  <div class="materials glass">
    <div class="material"><div class="name">Atlantis</div><div class="spec">Glass &nbsp;. &nbsp;00.00$ m2</div><div class="swatch" role="img" aria-label="Atlantis glass sample" style="background:linear-gradient(135deg,#9aa6a4,#4f5a58)"></div></div>
    <div class="material"><div class="name">Strata</div><div class="spec">Glass &nbsp;. &nbsp;00.00$ m2</div><div class="swatch" role="img" aria-label="Strata glass sample" style="background:linear-gradient(135deg,#7e9a98,#4c6462)"></div></div>
    <div class="material"><div class="name">Eska</div><div class="spec">Glass &nbsp;. &nbsp;00.00$ m2</div><div class="swatch" role="img" aria-label="Eska glass sample" style="background:linear-gradient(135deg,#a9b8a8,#66786a)"></div></div>
    <div class="material"><div class="name">Strialas</div><div class="spec">Glass &nbsp;. &nbsp;00.00$ m2</div><div class="swatch" role="img" aria-label="Strialas glass sample" style="background:linear-gradient(135deg,#6fa6a0,#3b6b66)"></div></div>
    <div class="material"><div class="name">Hitsu</div><div class="spec">Glass &nbsp;. &nbsp;00.00$ m2</div><div class="swatch" role="img" aria-label="Hitsu glass sample" style="background:linear-gradient(135deg,#7d8c84,#3d4a44)"></div></div>
    <div class="material"><div class="name">Grandeke</div><div class="spec">Glass &nbsp;. &nbsp;00.00$ m2</div><div class="swatch" role="img" aria-label="Grandeke glass sample" style="background:linear-gradient(135deg,#6e8a8e,#3c5256)"></div></div>
  </div>

  <footer class="footer">
    www.cellarqueen-example.com <span>.</span> info@cellarqueen-example.com <span>.</span> Tel: &nbsp;0800 555 0199
  </footer>
</main>
</body>
</html>
```